Business Cards
Stationary for Stainless Steel Abrasives distributor
Bright & Fun-filled
KV Grinding Inc. or Tamsel Bay Grinding Inc.
Avenida Corlinde Via 42 GT 9,
Villa Brezana,
Carolina, PR 00741
info@kelvoquartz.example
www.kelvoquartz.example
I would like to have a black business card with the same colors of my logos
Feel free to contact us for any questions or www.kelvoquartz.example
1. For the envelopes we want to use our postal address instead our physical address:
PO BOX 58314, MERUDA STATION, SAN JUAN PR 00637
2. Business Card use Postal Address plus Physical Address: use both
3. For the business paper we want the postal address that we mentioned in the #1
Cordially
This is the Logo you will be using for the stationary.
Another file you can use.

```html
<!DOCTYPE html>
<html lang="en">
<head>
<meta charset="utf-8">
<title>Tamsel Bay Grinding Inc. — Business Card</title>
<link rel="stylesheet" href="https://fonts.googleapis.com/css2?family=Cabin:wght@400;500&family=Roboto+Slab:wght@700&family=Libre+Baskerville:ital,wght@1,700&display=swap">
<style>
  :root {
    --page-bg: #e9e6e1;
    --card-black: #0b0b0c;
    --brand-blue: #27a8d8;
    --band-blue-light: #2aaed6;
    --band-blue-dark: #0a6d8d;
    --silver: #c9ccd0;
    --text-white: #f4f4f4;
  }
  * { box-sizing: border-box; margin: 0; padding: 0; }
  html, body { width: 1200px; height: 780px; overflow: hidden; }
  body { background: var(--page-bg); position: relative; font-family: "Cabin", sans-serif; }

  .business-card {
    position: absolute; left: 100px; top: 95px;
    width: 1000px; height: 590px;
    background: var(--card-black);
    border-radius: 30px;
    overflow: hidden;
    box-shadow: 0 14px 34px rgba(0,0,0,0.28);
  }
  .card-band { position: absolute; left: 0; top: 0; width: 1000px; height: 590px; }

  .brand-mark {
    position: absolute; left: 92px; top: 72px;
    width: 112px; height: 92px;
    background: var(--silver); border-radius: 10px;
  }
  .brand-divider {
    position: absolute; left: 232px; top: 64px; width: 2px; height: 108px;
    background: #5b5e62;
  }
  .brand-name {
    position: absolute; left: 256px; top: 58px;
    font-family: "Roboto Slab", serif; font-weight: 700;
    font-size: 48px; line-height: 56px; color: var(--brand-blue);
  }

  .address-block {
    position: absolute; right: 520px; top: 205px; text-align: right;
    color: var(--text-white); font-size: 22px; line-height: 28px;
  }
  .address-block .company {
    font-family: "Libre Baskerville", serif; font-style: italic; font-weight: 700;
    color: var(--brand-blue); font-size: 25px; line-height: 34px; margin-bottom: 8px;
  }
  .address-block .postal { margin-top: 12px; }

  .column-divider {
    position: absolute; left: 500px; top: 205px; width: 2px; height: 200px;
    background: linear-gradient(to bottom, rgba(180,180,180,0), #9a9da1 40%, rgba(180,180,180,0));
  }

  .contact-list {
    position: absolute; left: 530px; top: 240px; list-style: none;
    color: var(--text-white); font-size: 22px; line-height: 38px;
  }
  .contact-list li { display: flex; align-items: center; gap: 14px; }
  .contact-list svg { width: 21px; height: 21px; fill: var(--silver); flex: none; }

  .website {
    position: absolute; left: 0; width: 1000px; top: 530px; text-align: center;
    color: var(--text-white); font-size: 21px; font-weight: 500;
  }
</style>
</head>
<body>
  <div class="business-card">
    <svg class="card-band" viewBox="0 0 1000 590" aria-hidden="true">
      <defs>
        <linearGradient id="bandBlue" x1="0" y1="0" x2="0" y2="1">
          <stop offset="0" stop-color="#2aaed6"/>
          <stop offset="1" stop-color="#0a6d8d"/>
        </linearGradient>
        <linearGradient id="swooshSilver" x1="0" y1="0" x2="1" y2="0">
          <stop offset="0" stop-color="#55595c"/>
          <stop offset="0.6" stop-color="#ffffff"/>
          <stop offset="1" stop-color="#9a9ea2"/>
        </linearGradient>
      </defs>
      <path d="M0 498 Q520 478 1000 404 L1000 420 Q520 494 0 508 Z" fill="url(#swooshSilver)"/>
      <path d="M0 508 Q520 494 1000 420 L1000 590 L0 590 Z" fill="url(#bandBlue)"/>
    </svg>

    <div class="brand-mark"></div>
    <div class="brand-divider"></div>
    <div class="brand-name">Tamsel Bay<br>Grinding Inc.</div>

    <div class="address-block">
      <p class="company">KV Grinding Inc</p>
      <p>Pysical Avenida Corlinde</p>
      <p>Via 42 GT 9,Villa Brezana,</p>
      <p>Carolina, PR 00741</p>
      <p class="postal">Po Box 58314, Meruda Station,</p>
      <p>San juan PR 00637</p>
    </div>

    <div class="column-divider"></div>

    <ul class="contact-list">
      <li>
        <svg viewBox="0 0 24 24"><path d="M6.6 10.8a15.1 15.1 0 0 0 6.6 6.6l2.2-2.2c.3-.3.7-.4 1-.2 1.1.4 2.3.6 3.6.6.6 0 1 .4 1 1V20c0 .6-.4 1-1 1A17 17 0 0 1 3 4c0-.6.4-1 1-1h3.5c.6 0 1 .4 1 1 0 1.2.2 2.4.6 3.6.1.3 0 .7-.2 1z"/></svg>
        787-555-0142 / 787-555-0178
      </li>
      <li>
        <svg viewBox="0 0 24 24"><path d="M5 3h10v6h4v12H5zM7 5v4h6V5zm1 7h2v2H8zm4 0h2v2h-2zm-4 4h2v2H8zm4 0h2v2h-2zm4-4h1v6h-1z"/></svg>
        1866-555-0193
      </li>
      <li>
        <svg viewBox="0 0 24 24"><path d="M12 2a10 10 0 1 0 5 18.7l-1-1.7A8 8 0 1 1 20 12v1.2a1.8 1.8 0 0 1-3.6 0V12a4.4 4.4 0 1 0-1.3 3.1 3.8 3.8 0 0 0 6.9-1.9V12A10 10 0 0 0 12 2zm0 12.4a2.4 2.4 0 1 1 0-4.8 2.4 2.4 0 0 1 0 4.8z"/></svg>
        info@kelvoquartz.example
      </li>
    </ul>

    <p class="website">www.kelvoquartz.example</p>
  </div>
</body>
</html>
```